update company powerpoint deck - inject more power/personality into the deck

We would like a designer to provide us with a powerpoint template based on our brand guidelines. Current brand guidelines, colours and existing deck provided.
Current deck lacks punch. We really like our black and white elements - but need options for graphs, tables and charts. We potentially need more supplementary colours to what is currently in our brand guidelines.

Target Market(s)

listed companies - B2B. We are a management consulting company.

Industry/Entity Type

Consulting

Font styles to use
Serif
Sans Serif

Requirements
Must have
• Slides that are common for consulting companies.
The ability to use the deck as a report - not just a presentation format

```html
<!DOCTYPE html>
<html lang="en">
<head>
<meta charset="utf-8">
<title>Halver North – Master Slide Presentation</title>
<link href="https://fonts.googleapis.com/css2?family=Montserrat:wght@300;400;500;600;700&display=swap" rel="stylesheet">
<style>
:root{
  --teal:#80bdae;--teal-d:#5f9f90;--teal-l:#cfe5df;--ink:#121212;--grey:#8b8b8b;
  --line:#dcdcdc;--navy:#1f2a48;--red:#d3202e;--paper:#fff;--bg:#ffffff;
}
*{box-sizing:border-box}
html,body{margin:0;padding:0}
body{width:1200px;height:4481px;overflow:hidden;background:var(--bg);font-family:'Montserrat',sans-serif;color:var(--ink);position:relative}
.hero-slide{position:absolute;transform-origin:0 0}
.grid{position:absolute;top:1224px;left:22px;display:grid;grid-template-columns:repeat(3,371px);column-gap:21px;row-gap:24px}
.slide{width:371px;height:209px;position:relative;overflow:hidden;background:var(--paper);box-shadow:0 1px 5px rgba(0,0,0,.16)}
.slide.teal{background:var(--teal);color:#fff}
.slide.dark{background:var(--ink);color:#fff}
.slide.center-col{grid-column:2}
.abs{position:absolute}
.h{position:absolute;left:18px;top:15px;font-size:10px;font-weight:400;text-transform:uppercase;letter-spacing:.1px}
.dots{position:absolute;right:18px;top:17px;width:28px;height:7px;background-image:radial-gradient(#9a9a9a .8px,transparent 1px);background-size:4px 3.5px}
.dark .dots,.teal .dots{background-image:radial-gradient(#ddd .8px,transparent 1px)}
.foot{position:absolute;left:18px;bottom:8px;font-size:3.2px;color:#aaa;letter-spacing:.3px}
.pg{position:absolute;right:18px;bottom:8px;font-size:3.2px;color:#aaa}
.brand{font-weight:500;letter-spacing:6px;text-align:center;line-height:1.6;text-transform:uppercase}
.p{font-size:4px;line-height:1.5;color:#7a7a7a}
.dark .p,.teal .p{color:#e8e8e8}
.st{font-size:4.3px;font-weight:600;text-transform:uppercase;letter-spacing:.2px;margin-bottom:2px}
.st.t{color:var(--teal)}
.sub{font-size:4px;letter-spacing:2px;color:var(--teal);text-transform:uppercase}
.photo{position:absolute}
.sky{background:linear-gradient(160deg,#dfe8f0 0%,#9fb6cc 45%,#5d7d96 75%,#3d5b6e 100%)}
.city{background:linear-gradient(160deg,#4a4f55 0%,#23272b 55%,#0d0f10 100%)}
.office{background:linear-gradient(140deg,#bfc6cc 0%,#6f7a83 50%,#2e3740 100%)}
.portrait{background:linear-gradient(180deg,#c9c9c9,#8d8d8d)}
.pill{position:absolute;border:.6px solid #888;border-radius:6px;font-size:3.4px;letter-spacing:.8px;padding:2px 7px;text-transform:uppercase}
.num{color:var(--teal);font-size:9px;font-weight:300}
.row-line{border-bottom:.5px solid var(--line)}
.box{position:absolute}
svg{display:block}
</style>
</head>
<body>

<!-- Hero: featured slides -->
<div class="hero-slide" style="left:30px;top:40px;transform:scale(1.5)">
  <div class="slide dark">
    <div class="brand abs" style="right:20px;top:20px;font-size:7px">Halver<br>North</div>
    <div class="abs" style="left:18px;bottom:46px;font-size:34px;font-weight:300;color:var(--teal)">01</div>
    <div class="abs" style="left:70px;bottom:62px;font-size:10px;color:var(--teal);text-transform:uppercase">Section Title</div>
    <div class="abs p" style="left:70px;bottom:52px;width:240px">Get a modern presentation that is beautifully designed. Easy to change colors, photos and text.</div>
  </div>
</div>

<div class="hero-slide" style="left:614px;top:40px;transform:scale(1.5)">
  <div class="slide">
    <div class="dots" style="left:18px;right:auto;top:30px"></div>
    <div class="abs" style="left:18px;top:44px;font-size:10px;text-transform:uppercase;line-height:1.2">Mission<br>Statement</div>
    <div class="abs" style="left:150px;top:40px;font-size:30px;color:#ddd;font-weight:700">”</div>
    <div class="abs p" style="left:18px;top:76px;width:160px">You can simply impress your audience and add a unique zing and appeal to your presentations. Easy to change colors, photos and text. Get a modern presentation that is beautifully designed and easy to adapt for every meeting.</div>
    <div class="photo city" style="left:200px;top:0;width:171px;height:209px" role="img" aria-label="Photo of glass office towers at sunset"></div>
  </div>
</div>

<div class="hero-slide" style="left:210px;top:400px;transform:scale(2.05)">
  <div class="slide">
    <div class="photo sky" style="inset:0" role="img" aria-label="Photo of a statue against a cloudy sky"></div>
    <div class="brand abs" style="right:18px;top:16px;font-size:6px;color:#222">Halver<br>North</div>
    <div class="abs" style="right:18px;top:78px;font-size:3.6px;color:#333">Month 2021</div>
    <div class="abs" style="right:18px;top:86px;font-size:12px;text-align:right;line-height:1.15;color:#222;text-transform:uppercase">Master Slide<br>Presentation</div>
    <div class="abs sub" style="right:18px;top:117px;color:#555">Subtitle goes here</div>
    <div class="abs" style="right:18px;bottom:16px;font-size:3.4px;letter-spacing:1px;color:#333">PRESENTER NAME</div>
  </div>
</div>

<div class="hero-slide" style="left:30px;top:860px;transform:scale(1.5)">
  <div class="slide">
    <div class="abs" style="left:36px;top:55px;font-size:14px;text-transform:uppercase">Agenda</div>
    <div class="brand abs" style="left:36px;top:150px;font-size:5px;letter-spacing:4px">Halver<br>North</div>
    <div class="abs" style="left:205px;top:34px;width:148px">
      <div class="row-line" style="height:24px;font-size:4px;color:#666"><span class="num">01</span>&nbsp;&nbsp;&nbsp;Introduction</div>
      <div class="row-line" style="height:24px;font-size:4px;color:#666;margin-top:2px"><span class="num">02</span>&nbsp;&nbsp;&nbsp;About Us</div>
      <div class="row-line" style="height:24px;font-size:4px;color:#666;margin-top:2px"><span class="num">03</span>&nbsp;&nbsp;&nbsp;Welcome Message</div>
      <div class="row-line" style="height:24px;font-size:4px;color:#666;margin-top:2px"><span class="num">04</span>&nbsp;&nbsp;&nbsp;Our Services</div>
      <div class="row-line" style="height:24px;font-size:4px;color:#666;margin-top:2px"><span class="num">05</span>&nbsp;&nbsp;&nbsp;Our Team</div>
      <div style="height:24px;font-size:4px;color:#666;margin-top:2px"><span class="num">06</span>&nbsp;&nbsp;&nbsp;Contact Us</div>
    </div>
    <div class="pg">PAGE | 02</div>
  </div>
</div>

<div class="hero-slide" style="left:614px;top:860px;transform:scale(1.5)">
  <div class="slide teal">
    <div class="h">Our Latest Deals</div>
    <div class="abs" style="left:18px;top:44px;display:flex;gap:12px">
      <div style="width:75px;height:118px;border:.6px solid rgba(255,255,255,.7);text-align:center;padding-top:14px"><div style="width:18px;height:14px;background:#fff;margin:0 auto 14px"></div><div class="st">Contents Title</div><div class="p">Get a modern deck that is beautifully designed.</div></div>
      <div style="width:75px;height:118px;border:.6px solid rgba(255,255,255,.7);text-align:center;padding-top:14px"><div style="width:18px;height:14px;background:#fff;margin:0 auto 14px"></div><div class="st">Contents Title</div><div class="p">Get a modern deck that is beautifully designed.</div></div>
      <div style="width:75px;height:118px;border:.6px solid rgba(255,255,255,.7);text-align:center;padding-top:14px"><div style="width:18px;height:14px;background:#fff;margin:0 auto 14px"></div><div class="st">Contents Title</div><div class="p">Get a modern deck that is beautifully designed.</div></div>
      <div style="width:75px;height:118px;border:.6px solid rgba(255,255,255,.7);text-align:center;padding-top:14px"><div style="width:18px;height:14px;background:#fff;margin:0 auto 14px"></div><div class="st">Contents Title</div><div class="p">Get a modern deck that is beautifully designed.</div></div>
    </div>
    <div class="foot" style="color:#eee">HALVERNORTH.COM | COPYRIGHT 2021</div>
  </div>
</div>

<!-- Slide overview grid -->
<main class="grid">

  <section class="slide"><div class="brand abs" style="left:0;right:0;top:86px;font-size:9px">Halver<br>North</div></section>
  <section class="slide teal"><div class="brand abs" style="left:0;right:0;top:86px;font-size:9px">Halver<br>North</div></section>
  <section class="slide dark"><div class="brand abs" style="left:0;right:0;top:86px;font-size:9px">Halver<br>North</div></section>

  <section class="slide">
    <div class="brand abs" style="left:40px;top:92px;font-size:6px;letter-spacing:4px">Halver<br>North</div>
    <div class="abs" style="left:205px;top:34px;font-size:12px;line-height:1.15;text-transform:uppercase">Halver<br>North<br>Presentation</div>
    <div class="abs sub" style="left:205px;top:80px;font-size:3.4px">Subtitle goes here</div>
    <div class="abs" style="left:205px;top:94px;font-size:3px;color:var(--teal)">Month 2021</div>
    <div class="pill" style="left:205px;top:165px">Presenter Name</div>
  </section>

  <section class="slide">
    <div class="brand abs" style="left:40px;top:92px;font-size:6px;letter-spacing:4px">Halver<br>North</div>
    <div class="photo city" style="left:186px;top:0;width:185px;height:209px" role="img" aria-label="Dark photo of office buildings"></div>
    <div class="abs" style="left:205px;top:34px;font-size:12px;line-height:1.15;color:#fff;text-transform:uppercase">Halver<br>North<br>Presentation</div>
    <div class="abs sub" style="left:205px;top:80px;font-size:3.4px">Subtitle goes here</div>
    <div class="abs" style="left:205px;top:94px;font-size:3px;color:#ddd">Month 2021</div>
    <div class="pill" style="left:205px;top:165px;color:#fff;border-color:#ccc">Presenter Name</div>
  </section>

  <section class="slide">
    <div class="photo sky" style="inset:0" role="img" aria-label="Photo of a statue against a cloudy sky"></div>
    <div class="brand abs" style="right:18px;top:16px;font-size:6px;color:#222">Halver<br>North</div>
    <div class="abs" style="right:18px;top:78px;font-size:3.6px;color:#333">Month 2021</div>
    <div class="abs" style="right:18px;top:86px;font-size:12px;text-align:right;line-height:1.15;color:#222;text-transform:uppercase">Master Slide<br>Presentation</div>
    <div class="abs sub" style="right:18px;top:117px;color:#555">Subtitle goes here</div>
    <div class="abs" style="right:18px;bottom:16px;font-size:3.4px;letter-spacing:1px;color:#333">PRESENTER NAME</div>
  </section>

  <section class="slide dark">
    <div class="photo city" style="inset:0" role="img" aria-label="Dark photo of skyscrapers from below"></div>
    <div class="brand abs" style="left:0;right:0;top:16px;font-size:6px">Halver<br>North</div>
    <div class="abs" style="left:0;right:0;top:40px;text-align:center;font-size:3.4px;color:#ccc">www.halvernorth.com</div>
    <div class="abs" style="left:0;right:0;top:96px;text-align:center;font-size:14px;color:var(--teal);text-transform:uppercase">Master Slide Presentation</div>
    <div class="abs sub" style="left:0;right:0;top:118px;text-align:center;color:#ccc">Subtitle goes here</div>
    <div class="abs" style="left:0;right:0;top:136px;text-align:center;font-size:3.4px;color:#aaa;letter-spacing:1px">PRESENTER NAME</div>
  </section>

  <section class="slide">
    <div class="abs" style="left:36px;top:55px;font-size:14px;text-transform:uppercase">Agenda</div>
    <div class="brand abs" style="left:36px;top:150px;font-size:5px;letter-spacing:4px">Halver<br>North</div>
    <div class="abs" style="left:205px;top:34px;width:148px">
      <div class="row-line" style="height:24px;font-size:4px;color:#666"><span class="num">01</span>&nbsp;&nbsp;&nbsp;Introduction</div>
      <div class="row-line" style="height:24px;font-size:4px;color:#666;margin-top:2px"><span class="num">02</span>&nbsp;&nbsp;&nbsp;About Us</div>
      <div class="row-line" style="height:24px;font-size:4px;color:#666;margin-top:2px"><span class="num">03</span>&nbsp;&nbsp;&nbsp;Welcome Message</div>
      <div class="row-line" style="height:24px;font-size:4px;color:#666;margin-top:2px"><span class="num">04</span>&nbsp;&nbsp;&nbsp;Our Services</div>
      <div class="row-line" style="height:24px;font-size:4px;color:#666;margin-top:2px"><span class="num">05</span>&nbsp;&nbsp;&nbsp;Our Team</div>
      <div style="height:24px;font-size:4px;color:#666;margin-top:2px"><span class="num">06</span>&nbsp;&nbsp;&nbsp;Contact Us</div>
    </div>
    <div class="pg">PAGE | 02</div>
  </section>

  <section class="slide">
    <div class="h">Table of Content</div><div class="dots"></div>
    <div class="abs" style="left:40px;top:50px;display:grid;grid-template-columns:150px 150px;row-gap:14px">
      <div style="display:flex;gap:8px"><span style="font-size:22px;font-weight:300;color:#bbb">1</span><div><div class="st">Content Here</div><div class="p">Get a modern deck that is beautifully designed.</div></div></div>
      <div style="display:flex;gap:8px"><span style="font-size:22px;font-weight:300;color:#bbb">4</span><div><div class="st">Content Here</div><div class="p">Get a modern deck that is beautifully designed.</div></div></div>
      <div style="display:flex;gap:8px"><span style="font-size:22px;font-weight:300;color:#bbb">2</span><div><div class="st">Content Here</div><div class="p">Get a modern deck that is beautifully designed.</div></div></div>
      <div style="display:flex;gap:8px"><span style="font-size:22px;font-weight:300;color:#bbb">5</span><div><div class="st">Content Here</div><div class="p">Get a modern deck that is beautifully designed.</div></div></div>
      <div style="display:flex;gap:8px"><span style="font-size:22px;font-weight:300;color:#bbb">3</span><div><div class="st">Content Here</div><div class="p">Get a modern deck that is beautifully designed.</div></div></div>
      <div style="display:flex;gap:8px"><span style="font-size:22px;font-weight:300;color:#bbb">6</span><div><div class="st">Content Here</div><div class="p">Get a modern deck that is beautifully designed.</div></div></div>
    </div>
    <div class="pg">PAGE | 03</div>
  </section>

  <section class="slide dark">
    <div class="h">Introduction</div><div class="dots"></div>
    <div class="abs" style="left:42px;top:83px;width:46px;height:46px;border-radius:50%;border:.8px solid #666;display:flex;align-items:center;justify-content:center">
      <div style="width:30px;height:30px;border-radius:50%;background:var(--teal);color:#111;font-size:22px;font-weight:700;text-align:center;line-height:38px">”</div>
    </div>
    <div class="abs p" style="left:125px;top:88px;width:200px">You can simply impress your audience and add a unique zing and appeal to your presentations. Easy to change colors, photos and text. Get a modern presentation that is beautifully designed and easy to adapt.</div>
    <div class="abs" style="left:230px;top:132px;font-size:3.4px;color:#aaa">– NAME / ROLE / MANAGER</div>
    <div class="foot">HALVERNORTH.COM | COPYRIGHT 2021</div><div class="pg">PAGE | 04</div>
  </section>

  <section class="slide">
    <div class="h">Timeline</div><div class="dots"></div>
    <svg class="abs" style="left:0;top:0" width="371" height="209" viewBox="0 0 371 209">
      <line x1="38" y1="103" x2="330" y2="103" stroke="#999" stroke-width=".6"/>
      <g fill="#fff" stroke="#333" stroke-width=".8">
        <circle cx="90" cy="103" r="3"/><circle cx="125" cy="103" r="3"/><circle cx="160" cy="103" r="3"/><circle cx="195" cy="103" r="3"/><circle cx="230" cy="103" r="3"/><circle cx="265" cy="103" r="3"/>
      </g>
      <circle cx="330" cy="103" r="9" fill="#111"/>
      <text x="330" y="105" font-size="3.5" fill="#fff" text-anchor="middle" font-family="Montserrat">2021</text>
      <text x="28" y="98" font-size="7" fill="#333" font-family="Montserrat">Start</text>
      <text x="318" y="88" font-size="5" fill="#333" font-family="Montserrat">Vision</text>
      <g font-size="3" fill="#888" font-family="Montserrat" text-anchor="middle">
        <text x="90" y="112">2015</text><text x="125" y="96">2016</text><text x="160" y="112">2017</text><text x="195" y="96">2018</text><text x="230" y="112">2019</text><text x="265" y="96">2020</text>
      </g>
      <g fill="#bbb"><rect x="122" y="62" width="6" height="5"/><rect x="192" y="55" width="6" height="5"/><rect x="262" y="62" width="6" height="5"/><rect x="87" y="128" width="6" height="5"/><rect x="157" y="135" width="6" height="5"/><rect x="227" y="128" width="6" height="5"/></g>
    </svg>
    <div class="abs p" style="left:108px;top:70px;width:36px;text-align:center;font-size:3px">Content text here</div>
    <div class="abs p" style="left:177px;top:63px;width:36px;text-align:center;font-size:3px">Content text here</div>
    <div class="abs p" style="left:247px;top:70px;width:36px;text-align:center;font-size:3px">Content text here</div>
    <div class="abs p" style="left:72px;top:136px;width:36px;text-align:center;font-size:3px">Content text here</div>
    <div class="abs p" style="left:142px;top:143px;width:36px;text-align:center;font-size:3px">Content text here</div>
    <div class="abs p" style="left:212px;top:136px;width:36px;text-align:center;font-size:3px">Content text here</div>
    <div class="pg">PAGE | 05</div>
  </section>

  <section class="slide">
    <div class="h">Your Title Here - One Column</div><div class="dots"></div>
    <div class="abs" style="left:18px;top:58px;width:175px"><div class="st">Introduction</div><div class="p">You can simply impress your audience and add a unique zing and appeal to your presentations. Easy to change colors, photos and text. Get a modern presentation that is beautifully designed. You can simply impress your audience and add a unique zing and appeal to your presentations. Easy to change colors, photos and text.</div></div>
    <div class="foot">HALVERNORTH.COM | COPYRIGHT 2021</div><div class="pg">PAGE | 06</div>
  </section>

  <section class="slide">
    <div class="h">Your Title Here - Two Colum</div><div class="dots"></div>
    <div class="abs" style="left:18px;top:58px;width:150px"><div class="st">Content Here</div><div class="p">You can simply impress your audience and add a unique zing and appeal to your presentations. Easy to change colors, photos and text. Get a modern presentation that is beautifully designed and easy to adapt.</div></div>
    <div class="abs" style="left:190px;top:58px;width:150px"><div class="st t">Content Here</div><div class="p">You can simply impress your audience and add a unique zing and appeal to your presentations. Easy to change colors, photos and text. Get a modern presentation that is beautifully designed and easy to adapt.</div></div>
    <div class="foot">HALVERNORTH.COM | COPYRIGHT 2021</div><div class="pg">PAGE | 07</div>
  </section>

  <section class="slide">
    <div class="h">Your Title Here - Three Column</div><div class="dots"></div>
    <div class="abs" style="left:18px;top:58px;width:100px"><div class="st">Content Here</div><div class="p">You can simply impress your audience and add a unique zing and appeal to your presentations. Easy to change colors, photos and text.</div></div>
    <div class="abs" style="left:135px;top:58px;width:100px"><div class="st t">Content Here</div><div class="p">You can simply impress your audience and add a unique zing and appeal to your presentations. Easy to change colors, photos and text.</div></div>
    <div class="abs" style="left:252px;top:58px;width:100px"><div class="st">Content Here</div><div class="p">You can simply impress your audience and add a unique zing and appeal to your presentations. Easy to change colors, photos and text.</div></div>
    <div class="foot">HALVERNORTH.COM | COPYRIGHT 2021</div><div class="pg">PAGE | 08</div>
  </section>

  <section class="slide">
    <div class="h">Your Title Here</div><div class="abs sub" style="left:18px;top:28px;font-size:3.2px;letter-spacing:.5px">Subtitle Goes Here</div>
    <div class="abs" style="left:18px;top:58px;width:150px"><div class="st">Content Here</div><div class="p">You can simply impress your audience and add a unique zing and appeal to your presentations. Easy to change colors, photos and text. Get a modern presentation that is beautifully designed.</div></div>
    <div class="photo office" style="left:186px;top:55px;width:185px;height:120px" role="img" aria-label="Photo of a modern office interior"></div>
    <div class="abs" style="left:176px;top:62px;width:20px;height:90px;background:#111;display:flex;flex-direction:column;justify-content:space-around;align-items:center">
      <span style="width:8px;height:8px;border:.7px solid #fff"></span><span style="width:8px;height:8px;border:.7px solid var(--teal)"></span><span style="width:8px;height:8px;border:.7px solid #fff"></span>
    </div>
    <div class="abs" style="right:10px;top:160px;font-size:3.5px;color:#fff">Add your text here</div>
    <div class="pg">PAGE | 09</div>
  </section>

  <section class="slide">
    <div class="h">Bullets Points</div><div class="dots"></div>
    <div class="abs" style="left:18px;top:40px;display:grid;grid-template-columns:165px 165px;row-gap:10px">
      <div style="display:flex;gap:8px"><span style="width:10px;height:10px;background:#111;color:#fff;font-size:5px;text-align:center;line-height:10px;flex:none">1</span><div><div class="st">Content Title Here</div><div class="p">Get a modern deck that is beautifully designed.</div></div></div>
      <div style="display:flex;gap:8px"><span style="width:10px;height:10px;background:#111;color:#fff;font-size:5px;text-align:center;line-height:10px;flex:none">4</span><div><div class="st">Content Title Here</div><div class="p">Get a modern deck that is beautifully designed.</div></div></div>
      <div style="display:flex;gap:8px"><span style="width:10px;height:10px;background:var(--teal);color:#fff;font-size:5px;text-align:center;line-height:10px;flex:none">2</span><div><div class="st t">Content Title Here</div><div class="p">Get a modern deck that is beautifully designed.</div></div></div>
      <div style="display:flex;gap:8px"><span style="width:10px;height:10px;background:var(--teal);color:#fff;font-size:5px;text-align:center;line-height:10px;flex:none">5</span><div><div class="st t">Content Title Here</div><div class="p">Get a modern deck that is beautifully designed.</div></div></div>
      <div style="display:flex;gap:8px"><span style="width:10px;height:10px;background:var(--navy);color:#fff;font-size:5px;text-align:center;line-height:10px;flex:none">3</span><div><div class="st">Content Title Here</div><div class="p">Get a modern deck that is beautifully designed.</div></div></div>
      <div style="display:flex;gap:8px"><span style="width:10px;height:10px;background:var(--navy);color:#fff;font-size:5px;text-align:center;line-height:10px;flex:none">6</span><div><div class="st">Content Title Here</div><div class="p">Get a modern deck that is beautifully designed.</div></div></div>
    </div>
    <div class="pg">PAGE | 10</div>
  </section>

  <section class="slide">
    <div class="h">CEO Director</div><div class="dots"></div>
    <div class="photo portrait" style="left:24px;top:50px;width:56px;height:76px" role="img" aria-label="Portrait photo of the director"></div>
    <div class="abs" style="left:24px;top:134px;width:56px;text-align:center;font-size:3.5px">NAME HERE</div>
    <div class="abs" style="left:38px;top:142px;display:flex;gap:3px"><span style="width:5px;height:5px;border-radius:50%;background:#bbb"></span><span style="width:5px;height:5px;border-radius:50%;background:#bbb"></span><span style="width:5px;height:5px;border-radius:50%;background:#bbb"></span><span style="width:5px;height:5px;border-radius:50%;background:#bbb"></span></div>
    <div class="abs" style="left:105px;top:54px;width:110px"><div class="st">Content Here</div><div class="p">Get a modern deck that is beautifully designed. Easy to change colors.</div><div style="margin-top:5px;width:30px;border:.5px solid #999;font-size:3px;text-align:center;padding:1px">LEARN MORE</div></div>
    <div class="abs" style="left:225px;top:54px;width:110px"><div class="st t">Content Here</div><div class="p">Get a modern deck that is beautifully designed. Easy to change colors.</div></div>
    <div class="abs" style="left:105px;top:110px;width:240px">
      <div style="height:7px;background:#eee;margin-bottom:4px"><div style="width:82%;height:100%;background:#111;font-size:3px;color:#fff;padding-left:3px;line-height:7px">Content Title</div></div>
      <div style="height:7px;background:#eee"><div style="width:64%;height:100%;background:var(--teal);font-size:3px;color:#fff;padding-left:3px;line-height:7px">Content Title</div></div>
    </div>
    <div class="abs" style="right:20px;top:152px;font-size:3px;color:#888">hello@halvernorth.com</div>
    <div class="pg">PAGE | 11</div>
  </section>

  <section class="slide">
    <div class="h">Our Team</div><div class="dots"></div>
    <div class="abs" style="left:32px;top:44px;display:flex;gap:18px">
      <div style="width:62px"><div class="portrait" style="height:66px" role="img" aria-label="Team member photo"></div><div style="background:#111;color:#fff;font-size:3.5px;text-align:center;padding:2px">MEMBER NAME</div><div class="p" style="text-align:center;font-size:3.2px">Job title here, short bio text.</div></div>
      <div style="width:62px"><div class="portrait" style="height:66px" role="img" aria-label="Team member photo"></div><div style="background:var(--teal);color:#fff;font-size:3.5px;text-align:center;padding:2px">MEMBER NAME</div><div class="p" style="text-align:center;font-size:3.2px">Job title here, short bio text.</div></div>
      <div style="width:62px"><div class="portrait" style="height:66px" role="img" aria-label="Team member photo"></div><div style="background:#111;color:#fff;font-size:3.5px;text-align:center;padding:2px">MEMBER NAME</div><div class="p" style="text-align:center;font-size:3.2px">Job title here, short bio text.</div></div>
      <div style="width:62px"><div class="portrait" style="height:66px" role="img" aria-label="Team member photo"></div><div style="background:var(--teal);color:#fff;font-size:3.5px;text-align:center;padding:2px">MEMBER NAME</div><div class="p" style="text-align:center;font-size:3.2px">Job title here, short bio text.</div></div>
    </div>
    <div class="pg">PAGE | 12</div>
  </section>

  <section class="slide">
    <div class="h">Your Title Here</div><div class="dots"></div>
    <div class="abs" style="left:18px;top:52px;display:flex;gap:8px">
      <div style="width:76px;height:100px;box-shadow:0 0 3px rgba(0,0,0,.15);border-top:2px solid #111;position:relative;padding:5px"><div style="font-size:12px">01</div><div class="p">Lorem ipsum is simply dummy text of the printing industry.</div><div style="position:absolute;left:0;right:0;bottom:0;background:#111;color:#fff;font-size:3.5px;padding:2px 5px">OPTION NAME</div></div>
      <div style="width:76px;height:100px;box-shadow:0 0 3px rgba(0,0,0,.15);border-top:2px solid var(--teal);position:relative;padding:5px"><div style="font-size:12px;color:var(--teal)">02</div><div class="p">Lorem ipsum is simply dummy text of the printing industry.</div><div style="position:absolute;left:0;right:0;bottom:0;background:var(--teal);color:#fff;font-size:3.5px;padding:2px 5px">OPTION NAME</div></div>
      <div style="width:76px;height:100px;box-shadow:0 0 3px rgba(0,0,0,.15);border-top:2px solid var(--navy);position:relative;padding:5px"><div style="font-size:12px;color:var(--navy)">03</div><div class="p">Lorem ipsum is simply dummy text of the printing industry.</div><div style="position:absolute;left:0;right:0;bottom:0;background:var(--navy);color:#fff;font-size:3.5px;padding:2px 5px">OPTION NAME</div></div>
      <div style="width:76px;height:100px;box-shadow:0 0 3px rgba(0,0,0,.15);border-top:2px solid var(--red);position:relative;padding:5px"><div style="font-size:12px;color:var(--red)">04</div><div class="p">Lorem ipsum is simply dummy text of the printing industry.</div><div style="position:absolute;left:0;right:0;bottom:0;background:var(--red);color:#fff;font-size:3.5px;padding:2px 5px">OPTION NAME</div></div>
    </div>
    <div class="pg">PAGE | 13</div>
  </section>

  <section class="slide">
    <div class="h">Your Title Here - Infographic</div><div class="dots"></div>
    <svg class="abs" style="left:30px;top:48px" width="120" height="130" viewBox="0 0 120 130">
      <circle cx="45" cy="65" r="30" fill="#fff" stroke="#e4e4e4" stroke-width="6"/>
      <circle cx="88" cy="16" r="7" fill="#111"/><circle cx="100" cy="40" r="9" fill="var(--teal)"/><circle cx="98" cy="82" r="9" fill="var(--navy)"/><circle cx="86" cy="108" r="7" fill="#ddd"/>
      <text x="45" y="64" font-size="4" text-anchor="middle" font-family="Montserrat" letter-spacing="1.5">HALVER</text>
      <text x="45" y="70" font-size="4" text-anchor="middle" font-family="Montserrat" letter-spacing="1.5">NORTH</text>
    </svg>
    <div class="abs" style="left:190px;top:48px;width:150px;display:grid;row-gap:7px">
      <div><div class="st">✓ Content Title</div><div class="p">Get a modern deck that is beautifully designed.</div></div>
      <div><div class="st t">✓ Content Title</div><div class="p">Get a modern deck that is beautifully designed.</div></div>
      <div><div class="st" style="color:var(--navy)">✓ Content Title</div><div class="p">Get a modern deck that is beautifully designed.</div></div>
      <div><div class="st" style="color:var(--red)">✓ Content Title</div><div class="p">Get a modern deck that is beautifully designed.</div></div>
    </div>
    <div class="pg">PAGE | 14</div>
  </section>

  <section class="slide">
    <div class="h">Pie Charts</div><div class="dots"></div>
    <div class="abs p" style="left:18px;top:34px;width:300px">Get a clean &amp; modern presentation that is beautifully designed. Easy to change colors, photos and text.</div>
    <svg class="abs" style="left:0;top:70px" width="371" height="60" viewBox="0 0 371 60">
      <g fill="none" stroke-width="4" font-family="Montserrat">
        <circle cx="90" cy="30" r="14" stroke="#e6e6e6"/><circle cx="90" cy="30" r="14" stroke="var(--navy)" stroke-dasharray="59.8 88" transform="rotate(-90 90 30)"/>
        <circle cx="185" cy="30" r="14" stroke="#e6e6e6"/><circle cx="185" cy="30" r="14" stroke="var(--teal)" stroke-dasharray="30.8 88" transform="rotate(-90 185 30)"/>
        <circle cx="280" cy="30" r="14" stroke="#e6e6e6"/><circle cx="280" cy="30" r="14" stroke="var(--navy)" stroke-dasharray="48.4 88" transform="rotate(-90 280 30)"/>
      </g>
      <g font-size="7" text-anchor="middle" font-family="Montserrat"><text x="90" y="33" fill="#111">68%</text><text x="185" y="33" fill="var(--teal)">35%</text><text x="280" y="33" fill="var(--navy)">55%</text></g>
    </svg>
    <div class="abs p" style="left:60px;top:138px;width:60px;text-align:center">Get a modern deck that is beautifully designed.</div>
    <div class="abs p" style="left:155px;top:138px;width:60px;text-align:center">Get a modern deck that is beautifully designed.</div>
    <div class="abs p" style="left:250px;top:138px;width:60px;text-align:center">Get a modern deck that is beautifully designed.</div>
    <div class="pg">PAGE | 15</div>
  </section>

  <section class="slide">
    <div class="h">Infographic Style</div><div class="dots"></div>
    <div class="abs" style="left:36px;top:56px;font-size:38px;font-weight:300;line-height:1"><span style="font-size:18px;vertical-align:top">$</span>08</div>
    <div class="abs" style="left:84px;top:78px;background:#111;color:#fff;font-size:3px;padding:2px 5px">COST</div>
    <div class="abs" style="left:44px;top:96px;font-size:7px">MILLION</div>
    <div class="abs p" style="left:30px;top:108px;width:90px;text-align:center">Get a modern deck that is beautifully designed.</div>
    <div class="abs" style="left:190px;top:46px;font-size:30px;font-weight:300;color:var(--teal);line-height:1"><span style="font-size:14px;vertical-align:top">$</span>04</div>
    <div class="abs" style="left:236px;top:62px;background:var(--teal);color:#fff;font-size:3px;padding:2px 5px">RISE</div>
    <div class="abs" style="left:236px;top:74px;font-size:6px;color:var(--teal)">MILLION</div>
    <div class="abs p" style="left:290px;top:50px;width:60px">Get a modern deck that is beautifully designed.</div>
    <div class="abs" style="left:200px;top:118px;font-size:26px;font-weight:300;line-height:1">15<span style="font-size:10px;background:var(--teal);color:#fff;border-radius:50%;padding:0 2px">%</span></div>
    <div class="abs" style="left:250px;top:138px;background:var(--navy);color:#fff;font-size:3px;padding:2px 5px">PERCENTAGE</div>
    <div class="abs p" style="left:290px;top:124px;width:60px">Get a modern deck that is beautifully designed.</div>
    <div class="pg">PAGE | 16</div>
  </section>

  <section class="slide">
    <div class="h">Infographic Style</div><div class="dots"></div>
    <svg class="abs" style="left:130px;top:44px" width="110" height="130" viewBox="0 0 110 130">
      <polygon points="20,5 55,5 75,32 55,59 20,59 40,32" fill="var(--teal)"/>
      <polygon points="35,35 70,35 90,62 70,89 35,89 55,62" fill="#333"/>
      <polygon points="20,65 55,65 75,92 55,119 20,119 40,92" fill="#111"/>
      <polygon points="35,95 70,95 88,112 70,129 35,129 53,112" fill="var(--teal-d)"/>
      <g font-size="4" fill="#fff" font-family="Montserrat"><text x="44" y="34">STEP 01</text><text x="58" y="64">STEP 02</text><text x="44" y="94">STEP 03</text><text x="58" y="115">STEP 04</text></g>
    </svg>
    <div class="abs" style="left:30px;top:56px;width:95px;text-align:right"><div class="st t">Content Title</div><div class="p">Get a modern deck that is beautifully designed.</div></div>
    <div class="abs" style="left:30px;top:122px;width:95px;text-align:right"><div class="st">Content Title</div><div class="p">Get a modern deck that is beautifully designed.</div></div>
    <div class="abs" style="left:250px;top:56px;width:95px"><div class="st">Content Title</div><div class="p">Get a modern deck that is beautifully designed.</div></div>
    <div class="abs" style="left:250px;top:122px;width:95px"><div class="st t">Content Title</div><div class="p">Get a modern deck that is beautifully designed.</div></div>
    <div class="pg">PAGE | 17</div>
  </section>

  <section class="slide">
    <div class="h">Infographic Style</div><div class="abs sub" style="left:18px;top:28px;font-size:3.2px;letter-spacing:.5px">Subtitle Goes Here</div><div class="dots"></div>
    <svg class="abs" style="left:138px;top:48px" width="100" height="130" viewBox="0 0 100 130">
      <polygon points="50,0 100,14 50,28 0,14" fill="#111"/>
      <polygon points="50,28 100,42 50,56 0,42" fill="var(--teal)"/>
      <polygon points="50,56 100,70 50,84 0,70" fill="#111"/>
      <polygon points="50,84 100,98 50,112 0,98" fill="var(--teal)"/>
      <polygon points="50,104 100,118 50,130 0,118" fill="#222"/>
    </svg>
    <div class="abs" style="left:30px;top:50px;width:100px;text-align:right;display:grid;row-gap:8px">
      <div><div class="st">Content Title</div><div class="p">Get a modern deck that is beautifully designed.</div></div>
      <div><div class="st">Content Title</div><div class="p">Get a modern deck that is beautifully designed.</div></div>
      <div><div class="st t">Content Title</div><div class="p">Get a modern deck that is beautifully designed.</div></div>
    </div>
    <div class="abs" style="left:250px;top:70px;width:100px;display:grid;row-gap:8px">
      <div><div class="st t">Content Title</div><div class="p">Get a modern deck that is beautifully designed.</div></div>
      <div><div class="st">Content Title</div><div class="p">Get a modern deck that is beautifully designed.</div></div>
      <div><div class="st">Content Title</div><div class="p">Get a modern deck that is beautifully designed.</div></div>
    </div>
    <div class="pg">PAGE | 18</div>
  </section>

  <section class="slide">
    <div class="h">Infographic Style</div><div class="dots"></div>
    <svg class="abs" style="left:140px;top:42px" width="90" height="130" viewBox="0 0 90 130">
      <g fill="none" stroke-width="18">
        <circle cx="45" cy="65" r="34" stroke="var(--teal)" stroke-dasharray="40 2.7 40 2.7 40 2.7 40 2.7 40 2.7" />
        <circle cx="45" cy="65" r="34" stroke="var(--navy)" stroke-dasharray="40 174"/>
        <circle cx="45" cy="65" r="34" stroke="#111" stroke-dasharray="40 174" transform="rotate(144 45 65)"/>
      </g>
      <circle cx="45" cy="65" r="16" fill="#fff"/>
    </svg>
    <div class="abs" style="left:30px;top:48px;width:100px;text-align:right;display:grid;row-gap:6px">
      <div><div class="st t">Content Title</div><div class="p">Get a modern deck, beautifully designed.</div></div>
      <div><div class="st t">Content Title</div><div class="p">Get a modern deck, beautifully designed.</div></div>
      <div><div class="st">Content Title</div><div class="p">Get a modern deck, beautifully designed.</div></div>
      <div><div class="st t">Content Title</div><div class="p">Get a modern deck, beautifully designed.</div></div>
    </div>
    <div class="abs" style="left:245px;top:48px;width:100px;display:grid;row-gap:6px">
      <div><div class="st">Content Title</div><div class="p">Get a modern deck, beautifully designed.</div></div>
      <div><div class="st t">Content Title</div><div class="p">Get a modern deck, beautifully designed.</div></div>
      <div><div class="st">Content Title</div><div class="p">Get a modern deck, beautifully designed.</div></div>
      <div><div class="st t">Content Title</div><div class="p">Get a modern deck, beautifully designed.</div></div>
    </div>
    <div class="pg">PAGE | 19</div>
  </section>

  <section class="slide">
    <div class="h">SWOT Analysis</div><div class="dots"></div>
    <svg class="abs" style="left:135px;top:46px" width="100" height="120" viewBox="0 0 100 120">
      <g fill="none" stroke-width="9">
        <circle cx="50" cy="60" r="26" stroke="#111" stroke-dasharray="38 125.4" transform="rotate(-135 50 60)"/>
        <circle cx="50" cy="60" r="26" stroke="var(--teal)" stroke-dasharray="38 125.4" transform="rotate(-45 50 60)"/>
        <circle cx="50" cy="60" r="26" stroke="var(--navy)" stroke-dasharray="38 125.4" transform="rotate(45 50 60)"/>
        <circle cx="50" cy="60" r="26" stroke="#999" stroke-dasharray="38 125.4" transform="rotate(135 50 60)"/>
      </g>
      <g stroke="#ccc" stroke-width=".6" fill="#fff"><circle cx="50" cy="34" r="7"/><circle cx="76" cy="60" r="7"/><circle cx="50" cy="86" r="7"/><circle cx="24" cy="60" r="7"/></g>
      <g font-size="6" text-anchor="middle" font-family="Montserrat"><text x="50" y="36">S</text><text x="76" y="62" fill="var(--teal)">W</text><text x="50" y="88" fill="var(--navy)">O</text><text x="24" y="62">T</text></g>
    </svg>
    <div class="abs" style="left:30px;top:52px;width:100px;text-align:right"><div class="st">Strength</div><div class="p">Lorem ipsum dolor sit amet, consectetur adipiscing elit.</div></div>
    <div class="abs" style="left:30px;top:130px;width:100px;text-align:right"><div class="st">Threat</div><div class="p">Lorem ipsum dolor sit amet, consectetur adipiscing elit.</div></div>
    <div class="abs" style="left:245px;top:52px;width:100px"><div class="st t">Weakness</div><div class="p">Lorem ipsum dolor sit amet, consectetur adipiscing elit.</div></div>
    <div class="abs" style="left:245px;top:130px;width:100px"><div class="st">Opportunity</div><div class="p">Lorem ipsum dolor sit amet, consectetur adipiscing elit.</div></div>
    <div class="pg">PAGE | 20</div>
  </section>

  <section class="slide dark">
    <div class="brand abs" style="right:20px;top:20px;font-size:7px">Halver<br>North</div>
    <div class="abs" style="left:18px;bottom:46px;font-size:34px;font-weight:300;color:var(--teal)">01</div>
    <div class="abs" style="left:70px;bottom:62px;font-size:10px;color:var(--teal);text-transform:uppercase">Section Title</div>
    <div class="abs p" style="left:70px;bottom:52px;width:240px">Get a modern presentation that is beautifully designed. Easy to change colors, photos and text.</div>
  </section>

  <section class="slide teal">
    <div class="brand abs" style="right:20px;top:20px;font-size:7px">Halver<br>North</div>
    <div class="abs" style="left:18px;bottom:46px;font-size:34px;font-weight:300;color:#111">02</div>
    <div class="abs" style="left:70px;bottom:62px;font-size:10px;color:#111;text-transform:uppercase">Section Title</div>
    <div class="abs p" style="left:70px;bottom:52px;width:240px">Get a modern presentation that is beautifully designed. Easy to change colors, photos and text.</div>
  </section>

  <section class="slide">
    <div class="h">Bar Chart</div><div class="abs sub" style="left:18px;top:28px;font-size:3.2px;letter-spacing:.5px">Subtitle Goes Here</div><div class="dots"></div>
    <div class="abs p" style="left:40px;top:40px;width:290px">Lorem ipsum dolor sit amet, consectetur adipiscing elit. Sed do eiusmod tempor incididunt ut labore.</div>
    <svg class="abs" style="left:30px;top:58px" width="320" height="120" viewBox="0 0 320 120">
      <g stroke="#eee" stroke-width=".5"><line x1="20" y1="10" x2="315" y2="10"/><line x1="20" y1="35" x2="315" y2="35"/><line x1="20" y1="60" x2="315" y2="60"/><line x1="20" y1="85" x2="315" y2="85"/><line x1="20" y1="110" x2="315" y2="110"/></g>
      <g font-size="3.5" fill="#888" font-family="Montserrat"><text x="2" y="12">100%</text><text x="4" y="37">75%</text><text x="4" y="62">50%</text><text x="4" y="87">25%</text><text x="6" y="112">0%</text></g>
      <g>
        <rect x="35" y="20" width="8" height="90" fill="#ddd"/><rect x="45" y="70" width="8" height="40" fill="#111"/>
        <rect x="70" y="30" width="8" height="80" fill="#ddd"/><rect x="80" y="55" width="8" height="55" fill="var(--teal)"/>
        <rect x="105" y="15" width="8" height="95" fill="#ddd"/><rect x="115" y="65" width="8" height="45" fill="var(--navy)"/>
        <rect x="140" y="40" width="8" height="70" fill="#ddd"/><rect x="150" y="50" width="8" height="60" fill="#111"/>
        <rect x="175" y="25" width="8" height="85" fill="#ddd"/><rect x="185" y="75" width="8" height="35" fill="var(--teal)"/>
        <rect x="210" y="35" width="8" height="75" fill="#ddd"/><rect x="220" y="60" width="8" height="50" fill="#111"/>
        <rect x="245" y="20" width="8" height="90" fill="#ddd"/><rect x="255" y="45" width="8" height="65" fill="var(--navy)"/>
        <rect x="280" y="30" width="8" height="80" fill="#ddd"/><rect x="290" y="70" width="8" height="40" fill="#111"/>
      </g>
      <g font-size="3.5" fill="#888" font-family="Montserrat" text-anchor="middle"><text x="44" y="117">2011</text><text x="79" y="117">2012</text><text x="114" y="117">2013</text><text x="149" y="117">2014</text><text x="184" y="117">2015</text><text x="219" y="117">2016</text><text x="254" y="117">2017</text><text x="289" y="117">2018</text></g>
    </svg>
    <div class="pg">PAGE | 21</div>
  </section>

  <section class="slide">
    <div class="h">Chart With Text</div><div class="dots"></div>
    <svg class="abs" style="left:30px;top:42px" width="200" height="140" viewBox="0 0 200 140">
      <text x="100" y="8" font-size="4" fill="#666" text-anchor="middle" font-family="Montserrat">Series 1</text>
      <g stroke="#eee" stroke-width=".5"><line x1="10" y1="20" x2="195" y2="20"/><line x1="10" y1="50" x2="195" y2="50"/><line x1="10" y1="80" x2="195" y2="80"/><line x1="10" y1="110" x2="195" y2="110"/></g>
      <g fill="#111"><rect x="20" y="50" width="3" height="60"/><rect x="40" y="70" width="3" height="40"/><rect x="60" y="40" width="3" height="70"/><rect x="80" y="85" width="3" height="25"/><rect x="100" y="60" width="3" height="50"/><rect x="120" y="30" width="3" height="80"/><rect x="140" y="75" width="3" height="35"/><rect x="160" y="55" width="3" height="55"/><rect x="180" y="90" width="3" height="20"/></g>
      <polyline points="22,80 42,60 62,90 82,70 102,85 122,65 142,95 162,75 182,100" fill="none" stroke="var(--teal)" stroke-width=".8"/>
      <polyline points="22,95 42,88 62,70 82,95 102,75 122,92 142,80 162,98 182,85" fill="none" stroke="#aaa" stroke-width=".8"/>
      <g font-size="3" fill="#888" font-family="Montserrat" text-anchor="middle"><text x="22" y="117">2011</text><text x="62" y="117">2013</text><text x="102" y="117">2015</text><text x="142" y="117">2017</text><text x="182" y="117">2019</text></g>
    </svg>
    <div class="abs" style="left:240px;top:42px;width:110px;height:120px;background:#111;padding:8px">
      <div class="st" style="color:#fff">Content 01</div>
      <div class="p">You can simply impress your audience and add a unique zing and appeal to your presentations. Easy to change colors, photos and text. Get a modern presentation that is beautifully designed.</div>
      <div style="margin-top:8px;width:40px;border:.5px solid #888;font-size:3px;text-align:center;padding:1px;color:#ccc">ADD YOUR TEXT</div>
    </div>
    <div class="pg">PAGE | 22</div>
  </section>

  <section class="slide">
    <div class="h">Table Chart - Option 01</div><div class="dots"></div>
    <div class="abs" style="left:58px;top:58px;width:14px;height:86px;background:#333;display:flex;flex-direction:column;justify-content:space-around;align-items:center">
      <span style="width:6px;height:6px;border:.6px solid #fff"></span><span style="width:6px;height:6px;border:.6px solid #fff"></span><span style="width:6px;height:6px;border:.6px solid #fff"></span><span style="width:6px;height:6px;border:.6px solid #fff"></span><span style="width:6px;height:6px;border:.6px solid #fff"></span>
    </div>
    <table class="abs" style="left:80px;top:42px;width:250px;border-collapse:collapse;font-size:3.2px;color:#666;text-align:center">
      <tr style="background:#111;color:#fff;height:9px"><td>YOUR NAME</td><td style="background:var(--teal)">YOUR NAME</td><td>YOUR NAME</td></tr>
      <tr style="height:17px;border-bottom:.5px solid #eee"><td>Add Contents Title</td><td>Add Contents Title</td><td>Add Contents Title</td></tr>
      <tr style="height:17px;border-bottom:.5px solid #eee"><td>Modern Presentation</td><td>Modern Presentation</td><td>Modern Presentation</td></tr>
      <tr style="height:17px;border-bottom:.5px solid #eee"><td>Add Contents Title</td><td>Add Contents Title</td><td>Add Contents Title</td></tr>
      <tr style="height:17px;border-bottom:.5px solid #eee"><td>Modern Presentation</td><td>Modern Presentation</td><td>Modern Presentation</td></tr>
      <tr style="height:17px"><td>Add Contents Title</td><td>Add Contents Title</td><td>Add Contents Title</td></tr>
    </table>
    <div class="pg">PAGE | 23</div>
  </section>

  <section class="slide">
    <div class="h">Table Chart - Option 02</div><div class="dots"></div>
    <table class="abs" style="left:28px;top:42px;width:316px;border-collapse:collapse;font-size:3.2px;color:#555;text-align:center">
      <tr style="background:#111;color:#fff;height:8px"><td></td><td>2015</td><td>2016</td><td>2017</td><td>2018</td><td>2019</td><td>2020</td></tr>
      <tr style="height:13px;border-bottom:.5px solid #eee"><td style="text-align:left">Add Contents Title</td><td>10.4</td><td>11.3</td><td>10.6</td><td>11.1</td><td>10.4</td><td>11.3</td></tr>
      <tr style="height:13px;border-bottom:.5px solid #eee"><td style="text-align:left">Modern Presentation</td><td>10.6</td><td>10.6</td><td>10.6</td><td>10.6</td><td>10.6</td><td>10.6</td></tr>
      <tr style="height:13px;border-bottom:.5px solid #eee"><td style="text-align:left">Add Contents Title</td><td>0.05</td><td>0.05</td><td>0.05</td><td>0.05</td><td>0.05</td><td>0.05</td></tr>
      <tr style="height:13px;border-bottom:.5px solid #eee"><td style="text-align:left">Modern Presentation</td><td>5.6</td><td>5.6</td><td>5.6</td><td>5.6</td><td>5.6</td><td>5.6</td></tr>
      <tr style="height:13px;border-bottom:.5px solid #eee"><td style="text-align:left">Add Contents Title</td><td>3.4</td><td>3.4</td><td>3.4</td><td>3.4</td><td>3.4</td><td>3.4</td></tr>
      <tr style="height:13px;border-bottom:.5px solid #eee"><td style="text-align:left">Modern Presentation</td><td>2.8</td><td>2.8</td><td>2.8</td><td>2.8</td><td>2.8</td><td>2.8</td></tr>
      <tr style="height:9px;background:#111;color:#fff"><td style="text-align:left">Total</td><td>2.1</td><td>2.1</td><td>2.1</td><td>2.1</td><td>2.1</td><td>2.1</td></tr>
    </table>
    <div class="pg">PAGE | 24</div>
  </section>

  <section class="slide">
    <div class="h">Our Structure</div><div class="dots"></div>
    <svg class="abs" style="left:30px;top:40px" width="150" height="150" viewBox="0 0 150 150">
      <g fill="none" stroke-width="20">
        <circle cx="75" cy="75" r="50" stroke="#111" stroke-dasharray="157 314" transform="rotate(90 75 75)"/>
        <circle cx="75" cy="75" r="50" stroke="var(--teal)" stroke-dasharray="94.2 314" transform="rotate(-90 75 75)"/>
        <circle cx="75" cy="75" r="50" stroke="var(--navy)" stroke-dasharray="31.4 314" transform="rotate(18 75 75)"/>
        <circle cx="75" cy="75" r="50" stroke="#ddd" stroke-dasharray="31.4 314" transform="rotate(54 75 75)"/>
      </g>
      <g font-size="6" fill="#fff" font-family="Montserrat" text-anchor="middle"><text x="32" y="78">50%</text><text x="112" y="52">30%</text><text x="120" y="102">10%</text><text x="98" y="120" fill="#111">10%</text></g>
    </svg>
    <div class="abs" style="left:215px;top:50px;width:130px;display:grid;row-gap:8px">
      <div class="p" style="border-left:1.5px solid #111;padding-left:5px">Get a clean &amp; modern presentation, beautifully designed.</div>
      <div class="p" style="border-left:1.5px solid var(--teal);padding-left:5px">Get a clean &amp; modern presentation, beautifully designed.</div>
      <div class="p" style="border-left:1.5px solid var(--navy);padding-left:5px">Get a clean &amp; modern presentation, beautifully designed.</div>
      <div class="p" style="border-left:1.5px solid #ddd;padding-left:5px">Get a clean &amp; modern presentation, beautifully designed.</div>
    </div>
    <div class="pg">PAGE | 25</div>
  </section>

  <section class="slide">
    <div class="h">Logos With Text</div><div class="dots"></div>
    <div class="abs" style="left:28px;top:48px;display:grid;grid-template-columns:repeat(3,56px);gap:8px">
      <div style="height:24px;box-shadow:0 0 3px rgba(0,0,0,.12);font-size:4px;display:flex;align-items:center;justify-content:center;gap:2px"><span style="width:4px;height:4px;background:#888"></span>Northwind</div>
      <div style="height:24px;box-shadow:0 0 3px rgba(0,0,0,.12);font-size:4px;display:flex;align-items:center;justify-content:center;gap:2px"><span style="width:4px;height:4px;background:#888"></span>Northwind</div>
      <div style="height:24px;box-shadow:0 0 3px rgba(0,0,0,.12);font-size:4px;display:flex;align-items:center;justify-content:center;gap:2px"><span style="width:4px;height:4px;background:#888"></span>Northwind</div>
      <div style="height:24px;box-shadow:0 0 3px rgba(0,0,0,.12);font-size:4px;display:flex;align-items:center;justify-content:center;gap:2px"><span style="width:4px;height:4px;background:#888"></span>Northwind</div>
      <div style="height:24px;box-shadow:0 0 3px rgba(0,0,0,.12);font-size:4px;display:flex;align-items:center;justify-content:center;gap:2px"><span style="width:4px;height:4px;background:#888"></span>Northwind</div>
      <div style="height:24px;box-shadow:0 0 3px rgba(0,0,0,.12);font-size:4px;display:flex;align-items:center;justify-content:center;gap:2px"><span style="width:4px;height:4px;background:#888"></span>Northwind</div>
      <div style="height:24px;box-shadow:0 0 3px rgba(0,0,0,.12);font-size:4px;display:flex;align-items:center;justify-content:center;gap:2px"><span style="width:4px;height:4px;background:#888"></span>Northwind</div>
      <div style="height:24px;box-shadow:0 0 3px rgba(0,0,0,.12);font-size:4px;display:flex;align-items:center;justify-content:center;gap:2px"><span style="width:4px;height:4px;background:#888"></span>Northwind</div>
      <div style="height:24px;box-shadow:0 0 3px rgba(0,0,0,.12);font-size:4px;display:flex;align-items:center;justify-content:center;gap:2px"><span style="width:4px;height:4px;background:#888"></span>Northwind</div>
    </div>
    <div class="abs" style="left:250px;top:48px;width:90px"><div class="st">Contents Title</div><div class="p">Get a modern deck that is beautifully designed.</div></div>
    <div class="abs" style="left:335px;top:48px;width:14px;height:14px;background:#111"></div>
    <div class="abs" style="left:250px;top:100px;width:90px"><div class="st">Contents Title</div><div class="p">Get a modern deck that is beautifully designed.</div></div>
    <div class="abs" style="left:335px;top:100px;width:14px;height:14px;background:#ccc"></div>
    <div class="pg">PAGE | 26</div>
  </section>

  <section class="slide">
    <div class="photo office" style="left:0;top:0;width:186px;height:209px" role="img" aria-label="Photo of a hand signing documents"></div>
    <div class="abs" style="left:104px;top:12px;font-size:10px;color:#fff;text-transform:uppercase">Case Study</div>
    <div class="abs" style="left:0;top:140px;width:186px;height:69px;background:rgba(17,17,17,.85);padding:10px 14px">
      <div style="width:10px;height:10px;border-radius:50%;background:var(--teal);margin-bottom:4px"></div>
      <div class="p" style="color:#eee">Lorem ipsum is simply dummy text of the printing and typesetting industry.</div>
      <div style="font-size:3px;color:#aaa;text-align:right;margin-top:3px">NAME HERE</div>
    </div>
    <div class="abs" style="left:200px;top:24px;width:150px;display:grid;row-gap:12px">
      <div style="display:flex;gap:8px"><span style="width:14px;height:14px;background:#eee;flex:none"></span><div><div class="st">Challenges</div><div class="p">Get a clean &amp; modern presentation that is beautifully designed.</div></div></div>
      <div style="display:flex;gap:8px"><span style="width:14px;height:14px;background:var(--teal);flex:none"></span><div><div class="st t">Solution</div><div class="p">Get a clean &amp; modern presentation that is beautifully designed.</div></div></div>
      <div style="display:flex;gap:8px"><span style="width:14px;height:14px;background:#111;flex:none"></span><div><div class="st">Result</div><div class="p">Get a clean &amp; modern presentation that is beautifully designed.</div></div></div>
    </div>
    <div class="pg">PAGE | 27</div>
  </section>

  <section class="slide">
    <div class="dots" style="left:18px;right:auto;top:30px"></div>
    <div class="abs" style="left:18px;top:44px;font-size:10px;text-transform:uppercase;line-height:1.2">Mission<br>Statement</div>
    <div class="abs" style="left:150px;top:40px;font-size:30px;color:#ddd;font-weight:700">”</div>
    <div class="abs p" style="left:18px;top:76px;width:160px">You can simply impress your audience and add a unique zing and appeal to your presentations. Easy to change colors, photos and text. Get a modern presentation that is beautifully designed and easy to adapt for every meeting.</div>
    <div class="photo city" style="left:200px;top:0;width:171px;height:209px" role="img" aria-label="Photo of glass office towers at sunset"></div>
  </section>

  <section class="slide teal">
    <div class="h">Our Latest Deals</div>
    <div class="abs" style="left:18px;top:44px;display:flex;gap:12px">
      <div style="width:75px;height:118px;border:.6px solid rgba(255,255,255,.7);text-align:center;padding-top:14px"><div style="width:18px;height:14px;background:#fff;margin:0 auto 14px"></div><div class="st">Contents Title</div><div class="p">Get a modern deck that is beautifully designed.</div></div>
      <div style="width:75px;height:118px;border:.6px solid rgba(255,255,255,.7);text-align:center;padding-top:14px"><div style="width:18px;height:14px;background:#fff;margin:0 auto 14px"></div><div class="st">Contents Title</div><div class="p">Get a modern deck that is beautifully designed.</div></div>
      <div style="width:75px;height:118px;border:.6px solid rgba(255,255,255,.7);text-align:center;padding-top:14px"><div style="width:18px;height:14px;background:#fff;margin:0 auto 14px"></div><div class="st">Contents Title</div><div class="p">Get a modern deck that is beautifully designed.</div></div>
      <div style="width:75px;height:118px;border:.6px solid rgba(255,255,255,.7);text-align:center;padding-top:14px"><div style="width:18px;height:14px;background:#fff;margin:0 auto 14px"></div><div class="st">Contents Title</div><div class="p">Get a modern deck that is beautifully designed.</div></div>
    </div>
    <div class="foot" style="color:#eee">HALVERNORTH.COM | COPYRIGHT 2021</div>
  </section>

  <section class="slide">
    <div class="h">Free Icons</div><div class="dots"></div>
    <div class="abs" style="left:18px;top:38px;width:335px;height:150px;background:repeating-linear-gradient(90deg,#f1f1f1 0 8px,#fff 8px 12px)" role="img" aria-label="Library of line icons"></div>
    <div class="pg">PAGE | 29</div>
  </section>

  <section class="slide">
    <div class="dots" style="left:18px;right:auto;top:22px"></div>
    <div class="abs" style="left:18px;top:34px;font-size:11px;text-transform:uppercase">Thank You</div>
    <div class="abs sub" style="left:18px;top:52px;font-size:3.2px;letter-spacing:.5px">Presenter Name</div>
    <div class="abs" style="left:18px;top:70px;display:grid;row-gap:7px;font-size:3.8px;color:#555">
      <div style="display:flex;gap:5px;align-items:center"><span style="width:6px;height:6px;border-radius:50%;background:#111"></span>+00 000 000 000</div>
      <div style="display:flex;gap:5px;align-items:center"><span style="width:6px;height:6px;border-radius:50%;background:#111"></span>www.halvernorth.com</div>
      <div style="display:flex;gap:5px;align-items:center"><span style="width:6px;height:6px;border-radius:50%;background:#111"></span>hello@halvernorth.com</div>
      <div style="display:flex;gap:5px;align-items:center"><span style="width:6px;height:6px;border-radius:50%;background:#111"></span>Add your location here</div>
    </div>
    <div class="brand abs" style="right:30px;top:98px;font-size:6px;letter-spacing:4px">Halver<br>North</div>
  </section>

  <section class="slide center-col">
    <div class="h">Color Pallet</div><div class="dots"></div>
    <div class="abs" style="left:30px;top:42px;display:grid;grid-template-columns:repeat(7,26px);column-gap:16px;row-gap:8px">
      <span style="height:24px;background:#111"></span><span style="height:24px;background:#ddd"></span><span style="height:24px;background:#eee"></span><span style="height:24px;background:#555"></span><span style="height:24px;background:#888"></span><span style="height:24px;background:#ddd"></span><span style="height:24px;background:#444"></span>
      <span style="height:24px;background:var(--teal)"></span><span style="height:24px;background:var(--teal-l)"></span><span style="height:24px;background:#e8f1ee"></span><span style="height:24px;background:#aaa"></span><span style="height:24px;background:#ccc"></span><span style="height:24px;background:#f0d6e2"></span><span style="height:24px;background:#e6e6f2"></span>
      <span style="height:24px;background:var(--teal-d)"></span><span style="height:24px;background:#b8d8cf"></span><span style="height:24px;background:#d4d4d4"></span><span style="height:24px;background:var(--navy)"></span><span style="height:24px;background:#e3aac6"></span><span style="height:24px;background:#8b6bb0"></span><span style="height:24px;background:#e9e9f6"></span>
      <span style="height:24px;background:#666"></span><span style="height:24px;background:#333"></span><span style="height:24px;background:#222"></span><span style="height:24px;background:#2b2b2b"></span><span style="height:24px;background:#4a2f7a"></span><span style="height:24px;background:var(--red)"></span><span style="height:24px;background:#f1f1f1"></span>
    </div>
    <div class="pg">PAGE | 30</div>
  </section>

</main>
</body>
</html>
```